Design a Word Template and Powerpoint Template for a Venture Capital Fund

I'm looking to get a powerpoint template and word template designed ASAP under the same selected design. Its for a finance / Venture Capital business... keen to keep it clean but "pop" and stand up on its own as a strong brand, solid templates etc... Happy to talk. Thanks Lou

Target Market(s)

Venture Capital and Private Equity

Industry/Entity Type

Finance / Venture Capital / Management Consulting

Requirements
Nice to have
• Strong formatting, icons and optionality, images can be good too

```html
<!DOCTYPE html>
<html lang="en">
<head>
<meta charset="utf-8">
<title>Northfield Capital Group – Presentation Template</title>
<link href="https://fonts.googleapis.com/css2?family=Montserrat:wght@400;500;600&family=Open+Sans:wght@400;600&display=swap" rel="stylesheet">
<style>
:root{
  --stage:#3b3b3b;
  --ink:#1f1f1f;
  --ink-soft:#555;
  --paper:#ffffff;
  --night:#1c1c1c;
  --night-2:#2a2a2a;
  --rule:#8a8a8a;
  --muted:#9a9a9a;
}
*{box-sizing:border-box;margin:0;padding:0}
html,body{width:1200px;height:550px;overflow:hidden;background:var(--stage)}
body{position:relative;font-family:"Open Sans",Arial,sans-serif;color:var(--ink)}
.slide{position:absolute;width:321px;height:181px;overflow:hidden;background:var(--paper);box-shadow:0 3px 8px rgba(0,0,0,.45)}
.slide--cover{left:86px;top:78px;background:var(--night)}
.slide--service{left:439px;top:78px}
.slide--vision{left:793px;top:75px}
.slide--strategy{left:86px;top:295px}
.slide--works{left:439px;top:295px}
.slide--contact{left:793px;top:295px;background:var(--night)}
.abs{position:absolute}
.photo{position:absolute}
.heading{font-family:"Montserrat",Arial,sans-serif;font-weight:500;letter-spacing:.08em;text-transform:uppercase;color:var(--ink)}
.body-copy{font-size:3.2px;line-height:1.45;color:var(--ink-soft)}
.body-copy p+p{margin-top:5px}
.footer-brand{position:absolute;left:6px;bottom:6px;font-family:"Montserrat",Arial,sans-serif;line-height:1}
.footer-brand .name{font-size:5.6px;font-weight:500;letter-spacing:.06em;color:var(--ink)}
.footer-brand .sub{font-size:2.6px;letter-spacing:.35em;color:var(--ink-soft);margin-top:1px}
.footer-rule{position:absolute;left:56px;right:30px;bottom:7px;height:.6px;background:var(--ink)}
.footer-mark{position:absolute;right:7px;bottom:6px;font-family:"Montserrat",Arial,sans-serif;font-weight:500;font-size:11px;letter-spacing:.05em;color:var(--ink)}
.v-rule{position:absolute;width:.6px;background:var(--rule)}
/* cover */
.cover-photo{inset:0;background:radial-gradient(ellipse at 72% 45%,#555 0%,#3a3a3a 35%,#222 75%)}
.cover-brand{left:18px;top:30px;font-family:"Montserrat",Arial,sans-serif;color:#f2f2f2}
.cover-brand .name{font-size:11px;font-weight:500;letter-spacing:.06em}
.cover-brand .sub{font-size:4.4px;letter-spacing:.45em;text-align:center;margin-top:2px}
.cover-title{left:18px;top:110px;color:#f2f2f2;font-family:"Montserrat",Arial,sans-serif}
.cover-title .main{font-size:9px;letter-spacing:.05em}
.cover-title .main span{font-weight:400;text-transform:none;color:#cfcfcf}
.cover-title .tag{font-size:5px;color:#cfcfcf;font-family:"Open Sans",Arial,sans-serif}
.cover-copy{left:18px;top:132px;width:96px;font-size:2.6px;line-height:1.35;color:#d0d0d0}
.cover-copy p+p{margin-top:4px}
.cover-timeline{left:199px;top:139px;width:98px;color:#cfcfcf;font-size:2.6px}
.cover-timeline .label{font-size:2.8px;letter-spacing:.05em}
.cover-timeline .line{position:relative;height:.6px;background:#bbb;margin:6px 0 3px}
.cover-timeline .line i{position:absolute;top:-.7px;width:2px;height:2px;border-radius:50%;background:#ddd}
.cover-timeline .stops{display:flex;justify-content:space-between}
/* vision */
.vision-band{left:0;top:0;width:100%;height:72px;background:var(--night)}
.vision-title{left:0;width:100%;top:12px;text-align:center;font-family:"Montserrat",Arial,sans-serif;font-size:17px;font-weight:500;letter-spacing:.04em;color:#fff}
.vision-sub{left:0;width:100%;top:34px;text-align:center;font-size:4.4px;color:#ccc}
.vision-frame{left:92px;top:48px;width:137px;height:78px;background:#fff}
.vision-copy{left:80px;width:161px;top:135px;text-align:center}
</style>
</head>
<body>

<!-- Cover -->
<section class="slide slide--cover">
  <div class="photo cover-photo" role="img" aria-label="Dark monochrome photo of stacked coins with numbered markers"></div>
  <div class="abs cover-brand"><div class="name">NORTHFIELD</div><div class="sub">CAPITAL GROUP</div></div>
  <div class="abs cover-title">
    <div class="main">BUSINESS <span>strategy</span></div>
    <div class="tag">Presentation Template</div>
  </div>
  <div class="abs cover-copy">
    <p>Targets will rest on how you win and keep loyal clients.</p>
    <p>A clear plan shapes sharp messages that lift sales and grow results over time.</p>
  </div>
  <div class="abs cover-timeline">
    <div class="label">OUR SERVICE</div>
    <div class="line"><i style="left:0"></i><i style="left:49%"></i><i style="right:0"></i></div>
    <div class="stops"><span>Vision</span><span>Core Values</span><span>Success</span></div>
  </div>
</section>

<!-- Our service -->
<section class="slide slide--service">
  <h2 class="abs heading" style="left:21px;top:28px;font-size:8px">Our Service</h2>
  <div class="photo" style="left:21px;top:50px;width:137px;height:91px;background:linear-gradient(160deg,#e8e8e8 0%,#bfbfbf 45%,#5a5a5a 100%)" role="img" aria-label="Photo of a business team meeting around a table in a bright office"></div>
  <div class="v-rule" style="left:175px;top:56px;height:72px"></div>
  <h3 class="abs" style="left:182px;top:52px;font-family:'Montserrat',Arial,sans-serif;font-weight:400;font-size:9px;letter-spacing:.06em">about us</h3>
  <div class="abs body-copy" style="left:182px;top:67px;width:72px">
    <p>It is a process that lets a firm focus its resources on the best chances to grow sales and reach its target.</p>
    <p>Objectives rest on how you gain sales by winning and keeping clients.</p>
    <p>Lastly, progress should be measured and reviewed often so you know what works and what does not.</p>
  </div>
  <div class="footer-brand"><div class="name">NORTHFIELD</div><div class="sub">CAPITAL GROUP</div></div>
  <div class="footer-rule"></div>
  <div class="footer-mark">NCG</div>
</section>

<!-- Vision -->
<section class="slide slide--vision">
  <div class="abs vision-band"></div>
  <h2 class="abs vision-title">LOREM IPSUM</h2>
  <p class="abs vision-sub">Our works is the presentation of the our vision.</p>
  <div class="abs vision-frame"></div>
  <div class="photo" style="left:97px;top:53px;width:127px;height:71px;background:linear-gradient(180deg,#d9d9d9 0%,#8c8c8c 55%,#2e2e2e 100%)" role="img" aria-label="Monochrome photo of silhouetted people at a boardroom table before a world map"></div>
  <div class="abs body-copy vision-copy">
    <p>A clear plan shapes sharp messages that lift your sales outcome and marketing work.</p>
    <p>Objectives rest on how you gain sales by winning and keeping clients.</p>
  </div>
  <div class="footer-brand"><div class="name">NORTHFIELD</div><div class="sub">CAPITAL GROUP</div></div>
  <div class="footer-rule"></div>
  <div class="footer-mark">NCG</div>
</section>

<!-- Business strategy -->
<section class="slide slide--strategy">
  <h2 class="abs heading" style="left:24px;top:53px;font-size:9.5px">Business Strategy</h2>
  <div class="abs" style="left:24px;top:69px;width:162px;height:.6px;background:var(--rule)"></div>
  <div class="abs body-copy" style="left:24px;top:76px;width:42px"><p style="font-size:4px">01</p><p style="margin-top:2px">Strategy aims to lift sales and win an edge over rivals through short and long term steps.</p></div>
  <div class="abs body-copy" style="left:84px;top:76px;width:42px"><p style="font-size:4px">02</p><p style="margin-top:2px">A plan conveys clear messages with the right approach to grow sales results.</p></div>
  <div class="abs body-copy" style="left:143px;top:76px;width:42px"><p style="font-size:4px">03</p><p style="margin-top:2px">Timing the plan to fit buying cycles saves money and lifts sales. Follow up on each step.</p></div>
  <div class="photo" style="left:207px;top:68px;width:92px;height:52px;background:linear-gradient(135deg,#dfe6f2,#9fb3d6)" role="img" aria-label="Flat illustration of a team working together at a desk"></div>
  <div class="footer-brand"><div class="name">NORTHFIELD</div><div class="sub">CAPITAL GROUP</div></div>
  <div class="footer-rule"></div>
  <div class="footer-mark">NCG</div>
</section>

<!-- Core competence -->
<section class="slide slide--works">
  <h2 class="abs heading" style="left:18px;top:25px;font-size:7px;line-height:1.2">Our works is the presentation<br>&nbsp;of the our vision.</h2>
  <div class="photo" style="left:18px;top:50px;width:134px;height:94px;background:linear-gradient(150deg,#f0f0f0 0%,#a8a8a8 50%,#6a6a6a 100%)" role="img" aria-label="Monochrome photo of many hands stacked together"></div>
  <div class="v-rule" style="left:178px;top:48px;height:93px"></div>
  <h3 class="abs heading" style="left:185px;top:58px;font-size:7.5px;line-height:1.3">Core<br>Competence</h3>
  <div class="abs body-copy" style="left:185px;top:82px;width:68px;letter-spacing:.03em">
    <p>A plan conveys clear messages with the right approach to lift sales results.</p>
    <p>Objectives rest on how you gain sales by winning and keeping clients.</p>
  </div>
  <div class="footer-brand"><div class="name">NORTHFIELD</div><div class="sub">CAPITAL GROUP</div></div>
  <div class="footer-rule"></div>
  <div class="footer-mark">NCG</div>
</section>

<!-- Contact -->
<section class="slide slide--contact">
  <div class="abs" style="left:0;top:48px;width:100%;text-align:center;font-family:'Montserrat',Arial,sans-serif;color:#fff">
    <div style="font-size:19px;font-weight:500;letter-spacing:.06em;line-height:1">NORTHFIELD</div>
    <div style="font-size:7px;letter-spacing:.6em;margin-top:6px">CAPITAL GROUP</div>
  </div>
  <svg class="abs" style="left:35px;top:89px" width="252" height="4" viewBox="0 0 252 4" aria-hidden="true">
    <line x1="2" y1="2" x2="250" y2="2" stroke="#fff" stroke-width=".8"/>
    <circle cx="2" cy="2" r="1.8" fill="#fff"/><circle cx="126" cy="2" r="1.8" fill="#fff"/><circle cx="250" cy="2" r="1.8" fill="#fff"/>
  </svg>
  <div class="abs" style="left:0;top:103px;width:100%;text-align:center;color:#fff">
    <div style="font-size:9.5px">Lou Harlow</div>
    <div style="font-size:6.8px;margin-top:1px;display:flex;align-items:center;justify-content:center;gap:2px">
      <svg width="6" height="6" viewBox="0 0 10 10" aria-hidden="true"><circle cx="5" cy="5" r="5" fill="#fff"/><path d="M3.3 2.6l1 1-.5.8c.4.8 1 1.4 1.8 1.8l.8-.5 1 1-.6.9C5 7.4 2.6 5 2.4 3.2z" fill="#1c1c1c"/></svg>
      <span>+61 400 555 018</span>
    </div>
    <div style="font-size:6.8px;display:flex;align-items:center;justify-content:center;gap:2px">
      <svg width="6" height="6" viewBox="0 0 10 10" aria-hidden="true"><circle cx="5" cy="5" r="5" fill="#fff"/><rect x="2.5" y="3.3" width="5" height="3.4" fill="none" stroke="#1c1c1c" stroke-width=".7"/><path d="M2.5 3.3L5 5.3 7.5 3.3" fill="none" stroke="#1c1c1c" stroke-width=".7"/></svg>
      <span>lou@harlowmail.com</span>
    </div>
  </div>
</section>

</body>
</html>
```